Business card design for my trucking company

I would like a business card designed for my new trucking company. Please use my logo. the rest of the design is up to you. i would like my clients to say wow when they see the card. Im looking forward to seeing your designs

Target Market(s)

Industry/Entity Type

Trucking Company

Contact Information for Business Card

Marcus Tillbrook President
518-364-7120
ridgelinehaulage@examplemail.net

Font styles to use
Serif

Requirements
Must have
• my logo, name and number. we are located in Schenectady New York. the rest is up to you
Nice to have
• up to you
Should not have
• none

```html
<!DOCTYPE html>
<html lang="en">
<head>
<meta charset="utf-8">
<title>Ridgeline Haulage – Business Card</title>
<link rel="stylesheet" href="https://fonts.googleapis.com/css2?family=Playfair+Display:wght@400;700&display=swap">
<style>
  :root {
    --page-bg: #ececec;
    --card-bg: #ffffff;
    --ink: #111111;
    --steel: #6b6b6b;
    --shadow: rgba(0, 0, 0, 0.28);
  }
  * { margin: 0; padding: 0; box-sizing: border-box; }
  html, body {
    width: 846px;
    height: 1200px;
    overflow: hidden;
    background: var(--page-bg);
    font-family: "Playfair Display", Georgia, serif;
    color: var(--ink);
  }
  .canvas { position: relative; width: 846px; height: 1200px; }

  .card {
    position: absolute;
    left: 60px;
    width: 726px;
    height: 436px;
    background: var(--card-bg);
    box-shadow: -10px 10px 22px var(--shadow);
    overflow: hidden;
  }
  .card--front { top: 84px; }
  .card--back  { top: 603px; }

  /* Company wordmark (text only) */
  .wordmark {
    position: absolute;
    display: flex;
    align-items: center;
    gap: 14px;
    color: var(--ink);
    font-weight: 700;
    line-height: 1.05;
    text-transform: uppercase;
    letter-spacing: 0.04em;
  }
  .wordmark__square { background: var(--ink); flex: none; }
  .card--front .wordmark {
    left: 0; right: 0; top: 150px;
    justify-content: center;
    font-size: 38px;
  }
  .card--front .wordmark__square { width: 30px; height: 30px; }
  .card--back .wordmark {
    left: 52px; top: 176px;
    font-size: 21px;
  }
  .card--back .wordmark__square { width: 18px; height: 18px; }

  /* Back face */
  .person {
    position: absolute;
    right: 66px;
    top: 96px;
    text-align: right;
  }
  .person__name {
    font-size: 32px;
    font-weight: 700;
    color: var(--steel);
    line-height: 1.1;
  }
  .person__title {
    margin-top: 14px;
    font-size: 23px;
    font-weight: 400;
    letter-spacing: 0.02em;
    color: var(--ink);
  }
  .side-tab {
    position: absolute;
    right: 0;
    top: 107px;
    width: 24px;
    height: 57px;
    background: var(--steel);
  }
  .contacts {
    position: absolute;
    left: 190px;
    top: 333px;
    list-style: none;
  }
  .contacts__item {
    display: flex;
    align-items: center;
    height: 37px;
    font-size: 20px;
    font-weight: 700;
  }
  .contacts__item--email { font-weight: 400; font-size: 21px; }
  .contacts__icon {
    width: 26px;
    height: 22px;
    margin-right: 27px;
    flex: none;
  }
  .base-band {
    position: absolute;
    left: 144px;
    right: 0;
    bottom: 0;
    height: 24px;
    background: var(--steel);
  }
</style>
</head>
<body>
<main class="canvas">

  <section class="card card--front" aria-label="Card front">
    <div class="wordmark">
      <span class="wordmark__square"></span>
      <span class="wordmark__name">Ridgeline Haulage<br>&amp; Logistics Inc.</span>
    </div>
  </section>

  <section class="card card--back" aria-label="Card back">
    <div class="person">
      <p class="person__name">Marcus Tillbrook</p>
      <p class="person__title">PRESIDENT</p>
    </div>
    <div class="side-tab"></div>

    <div class="wordmark">
      <span class="wordmark__square"></span>
      <span class="wordmark__name">Ridgeline Haulage<br>&amp; Logistics Inc.</span>
    </div>

    <ul class="contacts">
      <li class="contacts__item">
        <svg class="contacts__icon" viewBox="0 0 26 22" aria-hidden="true">
          <path d="M1 8 Q13 -1 25 8 L22 11 L18 9 L18 6 Q13 4 8 6 L8 9 L4 11 Z" fill="#555"/>
          <path d="M5 12 L8 9 L18 9 L21 12 L22 21 L4 21 Z" fill="#555"/>
          <circle cx="13" cy="15" r="3.2" fill="#fff"/>
        </svg>
        <span>518-364-7120</span>
      </li>
      <li class="contacts__item contacts__item--email">
        <svg class="contacts__icon" viewBox="0 0 26 22" aria-hidden="true" fill="none" stroke="#555" stroke-width="1.2">
          <circle cx="13" cy="11" r="10"/>
          <ellipse cx="13" cy="11" rx="4.5" ry="10"/>
          <line x1="3" y1="11" x2="23" y2="11"/>
          <line x1="5" y1="5.5" x2="21" y2="5.5"/>
          <line x1="5" y1="16.5" x2="21" y2="16.5"/>
        </svg>
        <span>ridgelinehaulage@examplemail.net</span>
      </li>
    </ul>

    <div class="base-band"></div>
  </section>

</main>
</body>
</html>
```